Window company needs new banner

Window company that has 3 focuses needs a new banner ad.

We sell window hardware
We make new sashes and windows
We restore old windows

http://www.tlsashandrepair.example

I would like to create a new banner ad for our home page. The ad would try to capture the 3 sections listed above. I would also say they are listed in importance. Our main focus is hardware for this ad.

our best pictures are on our website.

Our suppliers websites
http://www.blenmar.example.uk
http://www.quillfittings.example.uk
https://www.daverlyworks.example

Target Market(s)

Historical buildings
Restoration contractors
window restorers
DIY home owners
custom window and door fabricators- Trades people

Industry/Entity Type

Home And Garden

Font styles to use
Serif

Requirements
Must have
• Show the high level of quality of our hardware and other services

```html
<!DOCTYPE html>
<html lang="en">
<head>
<meta charset="utf-8">
<title>Window Services Banners</title>
<link rel="stylesheet" href="https://fonts.googleapis.com/css2?family=Arimo:wght@400;700&display=swap">
<style>
  :root {
    --page-bg: #ffffff;
    --frame: #222222;
    --sky-grey: #eef0ef;
    --sky-blue: #cddcf4;
    --ribbon: #f4962a;
    --ribbon-fold: #d9801d;
    --curl: #ffffff;
    --caption: #111111;
    --photo-door: #8e8c84;
    --photo-casement: #a7927a;
    --photo-sash: #e7e7e3;
  }
  html, body {
    margin: 0;
    padding: 0;
    width: 1200px;
    height: 1200px;
    overflow: hidden;
    background: var(--page-bg);
    font-family: "Arimo", Arial, sans-serif;
  }
  .banner-stack {
    position: relative;
    width: 1200px;
    height: 1200px;
  }
  .banner {
    position: absolute;
    left: 284px;
    width: 646px;
  }
  .banner--hardware { top: 22px; }
  .banner--restoration { top: 414px; }
  .banner--sashes { top: 812px; }
  .banner__art {
    display: block;
    width: 646px;
    height: 352px;
    border: 1px solid var(--frame);
    box-sizing: border-box;
  }
  .banner__caption {
    margin: 6px 0 0;
    text-align: center;
    font-size: 14px;
    color: var(--caption);
  }
  .ribbon-text {
    font-family: "Arimo", Arial, sans-serif;
    font-weight: 700;
    font-size: 35px;
    fill: #ffffff;
  }
</style>
</head>
<body>
<svg width="0" height="0" style="position:absolute" aria-hidden="true">
  <defs>
    <filter id="text-shadow" x="-10%" y="-10%" width="130%" height="140%">
      <feDropShadow dx="2" dy="2" stdDeviation="1.5" flood-color="#7a3f00" flood-opacity="0.6"/>
    </filter>
    <filter id="ribbon-shadow" x="-10%" y="-10%" width="130%" height="130%">
      <feDropShadow dx="0" dy="4" stdDeviation="4" flood-color="#000" flood-opacity="0.18"/>
    </filter>
    <linearGradient id="tip-fade" x1="0" y1="0" x2="0" y2="1">
      <stop offset="0.7" stop-color="#f4962a"/>
      <stop offset="1" stop-color="#fbc27a"/>
    </linearGradient>
  </defs>
</svg>

<main class="banner-stack">
  <figure class="banner banner--hardware" style="margin:0">
    <svg class="banner__art" viewBox="0 0 808 440" preserveAspectRatio="none">
      <rect x="320" y="0" width="488" height="125" fill="var(--sky-grey)"/>
      <rect x="320" y="125" width="488" height="315" fill="var(--sky-blue)"/>
      <rect x="0" y="0" width="320" height="440" fill="var(--photo-door)" role="img" aria-label="Photo of an arched black double door window overlooking a snowy garden"/>
      <g filter="url(#ribbon-shadow)">
        <path d="M355 81 H807 V125 L400 398 C360 360 305 320 290 285 C278 250 292 215 330 182 C310 165 295 150 285 138 C310 110 330 90 355 81 Z" fill="url(#tip-fade)"/>
        <path d="M770 81 H807 V125 L745 125 Z" fill="var(--ribbon-fold)"/>
        <path d="M285 138 C300 152 318 168 333 182 C300 205 284 235 290 282 C272 240 268 180 285 138 Z" fill="var(--curl)"/>
      </g>
      <g class="ribbon-text" filter="url(#text-shadow)">
        <text x="353" y="145">Available</text>
        <text x="353" y="190">The Best Model</text>
        <text x="353" y="235">Of Windows</text>
        <text x="353" y="280">Hardware</text>
      </g>
    </svg>
    <figcaption class="banner__caption">New window for sale</figcaption>
  </figure>

  <figure class="banner banner--restoration" style="margin:0">
    <svg class="banner__art" viewBox="0 0 808 440" preserveAspectRatio="none">
      <rect x="320" y="0" width="488" height="125" fill="var(--sky-grey)"/>
      <rect x="320" y="125" width="488" height="315" fill="var(--sky-blue)"/>
      <rect x="0" y="0" width="320" height="440" fill="var(--photo-casement)" role="img" aria-label="Photo of a restored white casement window with brass fittings opening onto snowy trees"/>
      <g filter="url(#ribbon-shadow)">
        <path d="M355 81 H807 V125 L400 398 C360 360 305 320 290 285 C278 250 292 215 330 182 C310 165 295 150 285 138 C310 110 330 90 355 81 Z" fill="url(#tip-fade)"/>
        <path d="M770 81 H807 V125 L745 125 Z" fill="var(--ribbon-fold)"/>
        <path d="M285 138 C300 152 318 168 333 182 C300 205 284 235 290 282 C272 240 268 180 285 138 Z" fill="var(--curl)"/>
      </g>
      <g class="ribbon-text" filter="url(#text-shadow)">
        <text x="348" y="140">We provide</text>
        <text x="348" y="185">The Service of</text>
        <text x="348" y="230">Old Windows</text>
        <text x="348" y="275">Restoration</text>
      </g>
    </svg>
    <figcaption class="banner__caption">Old window restoration</figcaption>
  </figure>

  <figure class="banner banner--sashes" style="margin:0">
    <svg class="banner__art" viewBox="0 0 808 440" preserveAspectRatio="none">
      <rect x="320" y="0" width="488" height="125" fill="var(--sky-grey)"/>
      <rect x="320" y="125" width="488" height="315" fill="var(--sky-blue)"/>
      <rect x="0" y="0" width="320" height="440" fill="var(--photo-sash)" role="img" aria-label="Photo of a new painted sliding sash window with brass catches"/>
      <g filter="url(#ribbon-shadow)">
        <path d="M355 81 H807 V125 L400 398 C360 360 305 320 290 285 C278 250 292 215 330 182 C310 165 295 150 285 138 C310 110 330 90 355 81 Z" fill="url(#tip-fade)"/>
        <path d="M770 81 H807 V125 L745 125 Z" fill="var(--ribbon-fold)"/>
        <path d="M285 138 C300 152 318 168 333 182 C300 205 284 235 290 282 C272 240 268 180 285 138 Z" fill="var(--curl)"/>
      </g>
      <g class="ribbon-text" filter="url(#text-shadow)">
        <text x="356" y="145">We Make</text>
        <text x="356" y="190">New Sashes</text>
        <text x="356" y="235">and New</text>
        <text x="356" y="280">Windows</text>
      </g>
    </svg>
    <figcaption class="banner__caption">Make new sashes and windows</figcaption>
  </figure>
</main>
</body>
</html>
```